Calendar Design Project: 2025 with Specific Edits

This is a straightforward project where your creativity can shine!
Simply take the existing 2024 calendar and adapt it for 2025 by incorporating the new photos I've attached.
Please keep the overall concept of the 2024 calendar intact—your focus will be on enhancing it with fresh visuals.

I can't wait to see your amazing designs!
I am looking for a talented graphic designer to create a new 2025 calendar with specific adjustments.
Pictures attached.
Requirements:
Calendar Size: 52cm x 34cm
March Folder:
Adjust the image named "attached - DJI-0025" to make the circular road darker to match the rest of the design.
May Folder:
Modify the circled area in the May image to ensure it looks consistent with the other road (reference file: "attached - After").
November Folder:
Clear out the circled area in the November image (reference file: "attached - After1").
Please let me know if you have any questions or need further clarification.
I added to my breif a design i made last year for same client.
2025, calendar should be vertical and not horizontal. and some of the photos attache are "Before" and "After" please include together inside each month of the calendar.
Thank you!
Feel free to adjust any details as necessary!

Hello talented designers!

I’m excited to share that this is my 14th project on the ArtHarbor platform, and I’ve been fortunate to have successful collaborations in the past. I'm looking forward to creating a new 2025 calendar with your help, and I believe that with your creativity and skills, we can make this project a success as well!

I hope to establish a long-term relationship with a talented team like yours. As an added incentive, I will be offering a bonus for the winner, and I may select more than one winner, so everyone has a chance to shine!

Let’s make something amazing together!

Best
Update:
cancel or before, only place the After picture

Requirements
Must have
• Project Overview Objective: Create a 2025 calendar using the provided images, maintaining the design concept from the 2024 calendar but enhancing it with new visuals. Format: Vertical layout (52cm x 34cm).

```html
<!DOCTYPE html>
<html lang="en">
<head>
<meta charset="utf-8">
<title>KORVA Wall Calendar 2025 – March</title>
<link href="https://fonts.googleapis.com/css2?family=Roboto:wght@300;400;500;700&family=Open+Sans:wght@600;700&family=Pathway+Gothic+One&display=swap" rel="stylesheet">
<style>
  :root{
    --green:#2bb673;
    --green-deep:#1a6b3a;
    --lime:#8cc63f;
    --lime-soft:#c9e6a8;
    --weekend:#c9e6c0;
    --weekday:#ededed;
    --ink:#231f20;
    --grey:#555555;
    --paper:#ffffff;
  }
  *{box-sizing:border-box;margin:0;padding:0}
  html,body{width:785px;height:1200px;overflow:hidden;background:var(--paper)}
  .sheet{position:relative;width:785px;height:1200px;background:var(--paper);font-family:"Roboto",sans-serif;color:var(--ink)}
  .hero{position:absolute;left:0;top:0;width:785px;height:640px}
  .hero svg{display:block}
  .brand{position:absolute;left:56px;top:62px}
  .brand-name{display:flex;align-items:center;gap:10px;font-family:"Roboto",sans-serif;font-weight:700;font-size:64px;line-height:1;color:var(--ink);letter-spacing:1px}
  .brand-name .mark{width:34px;height:34px;background:var(--green)}
  .brand-tagline{margin-top:10px;font-size:10.5px;font-weight:400;color:var(--ink);letter-spacing:-.1px}
  .title-block{position:absolute;left:42px;top:590px}
  .title-label{font-size:31px;font-weight:400;color:var(--green);line-height:1;letter-spacing:-.5px}
  .title-year{font-size:72px;font-weight:700;line-height:1;letter-spacing:-2px;margin-top:2px}
  .month-name{position:absolute;left:318px;top:645px;font-size:47px;font-weight:400;color:var(--grey);letter-spacing:-1.5px;line-height:1}
  .main-grid{position:absolute;left:37px;top:706px;display:grid;grid-template-columns:repeat(7,66px);column-gap:4.7px;grid-template-rows:38px repeat(5,49px);row-gap:10px}
  .main-grid .head{display:flex;align-items:center;justify-content:center;font-family:"Open Sans",sans-serif;font-weight:600;font-size:9px;background:var(--weekday);color:var(--ink);margin-bottom:-1px}
  .main-grid .head.weekend{background:var(--weekend);color:var(--green-deep)}
  .day{position:relative;background:var(--weekday);font-weight:700;font-size:22px;line-height:1;padding:0 0 5px 3px;display:flex;align-items:flex-end}
  .day.weekend{background:var(--weekend);color:var(--green-deep)}
  .day.split{background-image:linear-gradient(to top right,transparent 49.3%,var(--paper) 49.6%,var(--paper) 50.4%,transparent 50.7%)}
  .day .late{position:absolute;right:3px;top:4px;color:var(--green-deep)}
  .mini{position:absolute;left:568px;width:184px}
  .mini-title{display:flex;align-items:center;font-size:14px;font-weight:500;letter-spacing:-.4px;height:18px}
  .mini-title .m{width:76px}
  .mini-title .y{border-left:2px solid #bbb;padding-left:6px;color:var(--green);font-weight:400;font-size:15px}
  .mini-grid{margin-top:8px;display:grid;grid-template-columns:repeat(7,24.5px);column-gap:1.8px;grid-template-rows:13px repeat(5,18px);row-gap:4px}
  .mini-grid .head{font-family:"Open Sans",sans-serif;font-size:3.4px;font-weight:600;display:flex;align-items:center;justify-content:center;background:var(--weekday)}
  .mini-grid .head.weekend{background:var(--weekend);color:var(--green-deep)}
  .mini-grid .d{background:var(--weekday);font-size:8px;font-weight:500;display:flex;align-items:flex-end;padding:0 0 2px 4px}
  .mini-grid .d.weekend{background:var(--weekend);color:var(--green-deep);font-weight:700}
  .footer{position:absolute;left:38px;top:1052px;width:715px;display:flex;align-items:flex-end;gap:18px}
  .footer-brand .name{display:flex;align-items:center;gap:4px;font-weight:700;font-size:20px;line-height:1}
  .footer-brand .name .mark{width:10px;height:10px;background:var(--green)}
  .footer-brand .tag{font-size:3.2px;margin-top:2px}
  .contacts{display:flex;gap:16px;font-family:"Pathway Gothic One",sans-serif;font-size:12.5px;color:var(--ink);padding-bottom:2px;white-space:nowrap}
  .contacts b{color:var(--green);font-weight:400}
</style>
</head>
<body>
<main class="sheet">
  <header class="hero">
    <svg width="785" height="640" viewBox="0 0 785 640">
      <defs>
        <linearGradient id="photoTone" x1="0" y1="0" x2="1" y2="1">
          <stop offset="0" stop-color="#8d8a80"/>
          <stop offset=".45" stop-color="#7a6a58"/>
          <stop offset=".7" stop-color="#6f7a62"/>
          <stop offset="1" stop-color="#8a6f55"/>
        </linearGradient>
        <linearGradient id="bandTop" x1="0" y1="0" x2="1" y2="0">
          <stop offset="0" stop-color="#eef7e2"/>
          <stop offset=".5" stop-color="var(--lime)"/>
          <stop offset="1" stop-color="var(--lime-soft)"/>
        </linearGradient>
        <linearGradient id="bandBottom" x1="0" y1="0" x2="1" y2="0">
          <stop offset="0" stop-color="#e8f4d8"/>
          <stop offset=".6" stop-color="var(--lime-soft)"/>
          <stop offset="1" stop-color="var(--lime)"/>
        </linearGradient>
      </defs>
      <rect class="hero-photo" x="0" y="80" width="785" height="480" fill="url(#photoTone)" role="img" aria-label="Aerial photograph of a newly built elevated road bridge crossing a river through a dense town of houses"/>
      <path d="M0,0H785V98C620,82 460,110 320,148C210,176 90,182 0,170Z" fill="url(#bandTop)"/>
      <path d="M0,58C130,20 310,28 440,78C340,132 200,186 0,168Z" fill="#ffffff"/>
      <path d="M0,548C220,500 470,528 785,462V640H0Z" fill="url(#bandBottom)"/>
      <path d="M0,560C150,546 300,574 460,606C580,630 690,636 785,634V640H0Z" fill="#ffffff"/>
    </svg>
    <div class="brand">
      <div class="brand-name"><span class="mark"></span>KORVA</div>
      <p class="brand-tagline">SOLID WORKS BUILD BETTER PLACES</p>
    </div>
  </header>

  <section class="title-block">
    <p class="title-label">CALENDAR</p>
    <p class="title-year">2025</p>
  </section>
  <h1 class="month-name">MARCH</h1>

  <section class="main-grid" aria-label="March 2025">
    <div class="head weekend">SUNDAY</div><div class="head">MONDAY</div><div class="head">TUESDAY</div><div class="head">WEDNESDAY</div><div class="head">THURSDAY</div><div class="head">FRIDAY</div><div class="head weekend">SATURDAY</div>
    <div class="day weekend"></div><div class="day"></div><div class="day"></div><div class="day"></div><div class="day"></div><div class="day"></div><div class="day weekend">1</div>
    <div class="day weekend">2</div><div class="day">3</div><div class="day">4</div><div class="day">5</div><div class="day">6</div><div class="day">7</div><div class="day weekend">8</div>
    <div class="day weekend">9</div><div class="day">10</div><div class="day">11</div><div class="day">12</div><div class="day">13</div><div class="day">14</div><div class="day weekend">15</div>
    <div class="day weekend">16</div><div class="day">17</div><div class="day">18</div><div class="day">19</div><div class="day">20</div><div class="day">21</div><div class="day weekend">22</div>
    <div class="day weekend split">23<span class="late">30</span></div><div class="day split">24<span class="late">31</span></div><div class="day">25</div><div class="day">26</div><div class="day">27</div><div class="day">28</div><div class="day weekend">29</div>
  </section>

  <section class="mini" style="top:702px" aria-label="February 2025">
    <h2 class="mini-title"><span class="m">FEBRUARY</span><span class="y">2025</span></h2>
    <div class="mini-grid">
      <div class="head weekend">SUNDAY</div><div class="head">MONDAY</div><div class="head">TUESDAY</div><div class="head">WEDNESDAY</div><div class="head">THURSDAY</div><div class="head">FRIDAY</div><div class="head weekend">SATURDAY</div>
      <div class="d weekend"></div><div class="d"></div><div class="d"></div><div class="d"></div><div class="d"></div><div class="d"></div><div class="d weekend">1</div>
      <div class="d weekend">2</div><div class="d">3</div><div class="d">4</div><div class="d">5</div><div class="d">6</div><div class="d">7</div><div class="d weekend">8</div>
      <div class="d weekend">9</div><div class="d">10</div><div class="d">11</div><div class="d">12</div><div class="d">13</div><div class="d">14</div><div class="d weekend">15</div>
      <div class="d weekend">16</div><div class="d">17</div><div class="d">18</div><div class="d">19</div><div class="d">20</div><div class="d">21</div><div class="d weekend">22</div>
      <div class="d weekend">23</div><div class="d">24</div><div class="d">25</div><div class="d">26</div><div class="d">27</div><div class="d">28</div><div class="d weekend"></div>
    </div>
  </section>

  <section class="mini" style="top:891px" aria-label="April 2025">
    <h2 class="mini-title"><span class="m" style="padding-left:14px">APRIL</span><span class="y">2025</span></h2>
    <div class="mini-grid">
      <div class="head weekend">SUNDAY</div><div class="head">MONDAY</div><div class="head">TUESDAY</div><div class="head">WEDNESDAY</div><div class="head">THURSDAY</div><div class="head">FRIDAY</div><div class="head weekend">SATURDAY</div>
      <div class="d weekend"></div><div class="d"></div><div class="d">1</div><div class="d">2</div><div class="d">3</div><div class="d">4</div><div class="d weekend">5</div>
      <div class="d weekend">6</div><div class="d">7</div><div class="d">8</div><div class="d">9</div><div class="d">10</div><div class="d">11</div><div class="d weekend">12</div>
      <div class="d weekend">13</div><div class="d">14</div><div class="d">15</div><div class="d">16</div><div class="d">17</div><div class="d">18</div><div class="d weekend">19</div>
      <div class="d weekend">20</div><div class="d">21</div><div class="d">22</div><div class="d">23</div><div class="d">24</div><div class="d">25</div><div class="d weekend">26</div>
      <div class="d weekend">27</div><div class="d">28</div><div class="d">29</div><div class="d">30</div><div class="d"></div><div class="d"></div><div class="d weekend"></div>
    </div>
  </section>

  <footer class="footer">
    <div class="footer-brand">
      <div class="name"><span class="mark"></span>KORVA</div>
      <p class="tag">SOLID WORKS BUILD BETTER PLACES</p>
    </div>
    <p class="contacts">
      <span><b>T</b>: +2340000512847</span>
      <span><b>E</b>: hello@korvabuild.com</span>
      <span><b>W</b>: www.korvabuild.com</span>
      <span><b>A</b>: 27 Palmgate Road, Off Harbour Close, Eastfield, Lakeview City</span>
    </p>
  </footer>
</main>
</body>
</html>
```